Presentation Folder Cover For Plumbing Company

We need a presentation folder cover (FRONT AND BACK) for our plumbing business.

We specialise in plumbing, hot water, electrical and pipe relining.

This will be sent to clients and the contents pages will outline all of our company details and information.

The target market for this cover is Strata / Property Managers who look after unit buildings.

Target Market(s)

Strata & Property Managers. The higher end of the property market.

Industry/Entity Type

Plumbing

Font styles to use
Sans Serif

Colors
ec1f27
0355a3
ffffff
474747
c9c9c9

Requirements
Must have
• A4 Paper Size
• Inviting to clients to open the document and read on.
Nice to have
• Sleek, Professional and Stands Out.
Should not have
• Dark Background. Needs to be fresh and bright.

```html
<!DOCTYPE html>
<html lang="en">
<head>
<meta charset="utf-8">
<title>Hartwell Contracting – Presentation Folder</title>
<link href="https://fonts.googleapis.com/css2?family=Arimo:wght@400;700&display=swap" rel="stylesheet">
<style>
  :root {
    --red: #ec1f27;
    --blue: #0355a3;
    --white: #ffffff;
    --charcoal: #474747;
    --silver: #c9c9c9;
    --ink: #2b2b2b;
    --sky-top: #e6f2fb;
    --sky-bottom: #f6fafd;
  }
  * { margin: 0; padding: 0; box-sizing: border-box; }
  html, body { width: 1200px; height: 777px; overflow: hidden; background: var(--white); }
  body { font-family: "Arimo", Arial, sans-serif; }

  .folder { position: relative; width: 1200px; height: 777px; display: flex; border: 1px solid #8a8a8a; }

  .back-cover {
    position: relative; width: 600px; height: 100%;
    background: linear-gradient(180deg, #ffffff 0%, #f4f4f4 100%);
    border-right: 1px solid #8a8a8a;
  }
  .front-cover {
    position: relative; width: 600px; height: 100%;
    background: radial-gradient(ellipse at 50% 45%, var(--sky-bottom) 0%, var(--sky-top) 100%);
  }

  .brand-name {
    color: var(--blue); font-weight: 700; text-transform: uppercase;
    line-height: 1.05; text-align: center; letter-spacing: 1px;
  }
  .front-cover .brand-name { position: absolute; left: 0; right: 0; top: 100px; font-size: 36px; }
  .back-cover .brand-name { position: absolute; left: 385px; top: 528px; font-size: 19px; }

  .tagline {
    position: absolute; left: 0; right: 0; top: 200px; text-align: center;
    font-size: 17px; font-weight: 700; color: var(--ink);
  }
  .website {
    position: absolute; left: 0; right: 0; top: 728px; text-align: center;
    font-size: 13px; font-weight: 700; color: var(--ink); letter-spacing: 9px;
  }

  .address-band {
    position: absolute; left: 177px; top: 598px; width: 423px; height: 83px;
    background: var(--blue);
  }
  .address-lines {
    position: absolute; left: 68px; top: 9px; color: var(--white);
    font-size: 12px; line-height: 14.3px; white-space: nowrap;
  }
  .collage { position: absolute; left: 0; top: 0; width: 600px; height: 777px; }
  .badge { position: absolute; left: 60px; top: 560px; width: 158px; height: 158px; }
</style>
</head>
<body>
<main class="folder">

  <section class="back-cover">
    <p class="brand-name">Hartwell<br>Contracting</p>
    <div class="address-band">
      <div class="address-lines">
        <p>AddressAddress Address Address Address Address</p>
        <p>AddressAddress Address Address Address Address</p>
        <p>AddressAddress Address Address Address Address</p>
        <p>AddressAddress Address Address Address Address</p>
        <p>AddressAddress Address Address Address Address</p>
      </div>
    </div>
    <svg class="badge" viewBox="0 0 158 158">
      <defs>
        <linearGradient id="badge-photo" x1="0" y1="0" x2="1" y2="1">
          <stop offset="0" stop-color="#c9573f"/>
          <stop offset="0.45" stop-color="#8a7d76"/>
          <stop offset="1" stop-color="#d8c2b2"/>
        </linearGradient>
      </defs>
      <polygon points="79,0 158,79 79,158 0,79" fill="#ffffff"/>
      <polygon role="img" aria-label="Photo of a plumber fitting pipework with a red wrench" points="79,21 137,79 79,137 21,79" fill="url(#badge-photo)"/>
    </svg>
  </section>

  <section class="front-cover">
    <p class="brand-name">Hartwell<br>Contracting</p>
    <p class="tagline">Plumbing • Electrical • Hot Water</p>

    <svg class="collage" viewBox="0 0 600 777">
      <defs>
        <linearGradient id="fold-light" x1="0" y1="0" x2="1" y2="1">
          <stop offset="0" stop-color="#f4f4f4"/>
          <stop offset="1" stop-color="#a3a3a3"/>
        </linearGradient>
        <linearGradient id="fold-dark" x1="1" y1="0" x2="0" y2="1">
          <stop offset="0" stop-color="#e8e8e8"/>
          <stop offset="1" stop-color="#7f7f7f"/>
        </linearGradient>
        <linearGradient id="fold-mid" x1="0" y1="1" x2="1" y2="0">
          <stop offset="0" stop-color="#8e8e8e"/>
          <stop offset="1" stop-color="#dedede"/>
        </linearGradient>
        <linearGradient id="photo-pipes" x1="0" y1="0" x2="1" y2="1">
          <stop offset="0" stop-color="#ebe7e4"/>
          <stop offset="0.35" stop-color="#c24a37"/>
          <stop offset="0.6" stop-color="#3a3a3a"/>
          <stop offset="1" stop-color="#d6b7a2"/>
        </linearGradient>
        <linearGradient id="photo-valve" x1="0" y1="0" x2="1" y2="1">
          <stop offset="0" stop-color="#5c5c5c"/>
          <stop offset="0.5" stop-color="#d0d0d0"/>
          <stop offset="1" stop-color="#777777"/>
        </linearGradient>
        <linearGradient id="photo-wiring" x1="0" y1="0" x2="1" y2="1">
          <stop offset="0" stop-color="#d8ad92"/>
          <stop offset="0.5" stop-color="#5f93c4"/>
          <stop offset="1" stop-color="#cfcac2"/>
        </linearGradient>
        <linearGradient id="photo-shower" x1="0" y1="0" x2="1" y2="1">
          <stop offset="0" stop-color="#f4f6f8"/>
          <stop offset="1" stop-color="#9aa3aa"/>
        </linearGradient>
        <linearGradient id="photo-filter" x1="0" y1="0" x2="1" y2="1">
          <stop offset="0" stop-color="#5f8fc0"/>
          <stop offset="0.55" stop-color="#cfe0ee"/>
          <stop offset="1" stop-color="#7fa8cf"/>
        </linearGradient>
        <radialGradient id="floor-shadow">
          <stop offset="0" stop-color="#9aa4ad" stop-opacity="0.55"/>
          <stop offset="1" stop-color="#9aa4ad" stop-opacity="0"/>
        </radialGradient>
      </defs>

      <ellipse cx="300" cy="684" rx="200" ry="20" fill="url(#floor-shadow)"/>

      <!-- folded silver panels -->
      <polygon points="327,268 405,346 327,424 249,346" fill="url(#fold-light)"/>
      <polygon points="120,380 220,280 270,330 170,430" fill="url(#fold-mid)"/>
      <polygon points="170,430 270,330 320,380 220,480" fill="url(#fold-dark)"/>
      <polygon points="300,590 370,520 440,590" fill="url(#fold-light)"/>
      <polygon points="300,590 440,590 370,660" fill="url(#fold-dark)"/>

      <!-- photo tiles -->
      <polygon role="img" aria-label="Photo of a chrome shower head with a falling water droplet" points="340,390 420,310 500,390 420,470" fill="url(#photo-shower)"/>
      <polygon role="img" aria-label="Photo of an electrician testing wiring in a switchboard" points="220,480 320,380 420,480 320,580" fill="url(#photo-wiring)"/>
      <polygon role="img" aria-label="Photo of a water filter cartridge" points="420,480 505,395 590,480 505,565" fill="url(#photo-filter)"/>
      <line x1="420" y1="480" x2="505" y2="395" stroke="var(--red)" stroke-width="3"/>
      <polygon role="img" aria-label="Photo of pipework being tightened with a red pipe wrench" points="20,480 120,380 220,480 120,580" fill="url(#photo-pipes)"/>
      <polygon role="img" aria-label="Black and white photo of a brass valve fitting" points="120,580 220,480 320,580 220,680" fill="url(#photo-valve)"/>
    </svg>

    <p class="website">www.website.com</p>
  </section>

</main>
</body>
</html>
```